I’d like to see something with similar colors and design concept to the “Your Fortune Starts at Breakfast” book included in attchment

Create a book cover with front cover, and full front, spine and back cover spread.
Simple and clean design. See design inspiration below.
Size 6X9
Title of the book: Write Onward! Veteran Editors Reveal Their Methods

Please leave space for 6 authors names on the front cover. Authors names will be provided at a later time.

Back of book should included the name of the publishing company:
Bright Lantern Publishing

As well as the following synopsis
The landscape of the publishing industry is changing. Gone are the days of coveted gatekeepers controlling content and dictating the messages being distributed. With the rise of technology, social media , self-publishing platforms, and independent bookstores, there are increased opportunities for people to share their ideas, messages, and stories with the world through books. The types of books that we’re publishing are also evolving — mini-books, audio books, journals, multi-author books, cook books, children’s books, comic books, coloring books, interactive books, tarot and oracle card decks are all expanding the podium for people to express ideas and influence the culture. More and more entrepreneurs are posturing themselves as thought leaders by leveraging this growing platform.
But that doesn't mean it’s easy.
Even with the expanding platforms and opportunities, only a fraction of people with publishing ambitions are able to achieve this coveted dream held by so many. It can be a daunting process for budding authors trying to maneuver through the writing, packaging, marketing, and publishing processes alone.

In this book you'll find passionate, purpose-driven, and well-versed experts working in the various areas of publishing, eager to help open your eyes to the promise of publishing and effortlessly guide you through the process.

Colors
0094D4
00A9DD
6FCCEA
C7EBF8
E9F6FB
FFF300
FFF600
FEFA6F
FFFEC7
FFFEE8
FFC000
F8CF3A
FAE287
FDF2CF
FEFAEE
F0912C
F2A743
F7CA91
FBE8D2
FDF5EE
EE7325
F08F49
F5BC92
FAE3D3
FDF4ED
6B429C
8869AF
B7A5CE
E3DAEB
F3F0F8

```html
<!DOCTYPE html>
<html lang="en">
<head>
<meta charset="utf-8">
<title>Write Onward! Veteran Editors Reveal Their Methods — Cover Spread</title>
<link rel="stylesheet" href="https://fonts.googleapis.com/css2?family=Montserrat:ital,wght@0,400;0,500;0,800;0,900;1,500&display=swap">
<style>
  :root {
    --red: #e6473b;
    --glow: #ef6a2a;
    --navy: #0d304a;
    --white: #ffffff;
    --shadow-orange: #f58a3f;
    --ink: #1c2633;
  }
  * { margin: 0; padding: 0; box-sizing: border-box; }
  html, body { width: 1200px; height: 867px; overflow: hidden; }
  body { font-family: "Montserrat", sans-serif; background: var(--red); }

  .spread {
    position: relative;
    width: 1200px;
    height: 867px;
    overflow: hidden;
    background:
      radial-gradient(ellipse 260px 300px at 290px 420px, rgba(239,106,42,0.9), rgba(239,106,42,0) 100%),
      radial-gradient(ellipse 320px 300px at 880px 360px, rgba(239,106,42,0.95), rgba(239,106,42,0) 100%),
      var(--red);
  }

  /* Back cover */
  .synopsis {
    position: absolute;
    left: 53px;
    top: 105px;
    width: 481px;
    font-size: 15.8px;
    line-height: 20.6px;
    font-weight: 400;
    color: var(--ink);
    text-align: justify;
    hyphens: auto;
  }
  .synopsis p.gap { margin-top: 20.6px; }
  .publisher {
    position: absolute;
    left: 159px;
    top: 804px;
    font-size: 22px;
    font-style: italic;
    font-weight: 500;
    color: var(--white);
  }

  /* Spine */
  .spine-title {
    position: absolute;
    left: 600px;
    top: 439px;
    transform: translate(-50%, -50%) rotate(-90deg);
    white-space: nowrap;
    font-size: 25px;
    font-weight: 800;
    color: var(--white);
    text-shadow: -2px 1px 0 var(--shadow-orange);
  }

  /* Front cover */
  .front-title {
    position: absolute;
    left: 661px;
    top: 30px;
    font-weight: 900;
    font-size: 50px;
    line-height: 67px;
    letter-spacing: -1px;
    text-transform: uppercase;
    white-space: nowrap;
  }
  .front-title span { display: block; text-shadow: -3px 3px 0 var(--shadow-orange); }
  .front-title .lead { color: var(--white); }
  .front-title .line { color: var(--navy); }

  .book-art { position: absolute; left: 0; top: 0; width: 1200px; height: 867px; pointer-events: none; }
  .book-art .page-light {
    position: absolute;
    left: 669px;
    top: 446px;
    width: 245px;
    height: 387px;
    background: var(--white);
    box-shadow: 0 0 14px 4px rgba(255,220,190,0.7);
  }
  .book-art .page-dark {
    position: absolute;
    left: 930px;
    top: 440px;
    width: 238px;
    height: 334px;
    background: var(--navy);
  }

  .authors {
    position: absolute;
    left: 940px;
    top: 497px;
    list-style: none;
    color: var(--white);
    font-size: 21px;
    font-weight: 500;
    line-height: 37px;
  }
</style>
</head>
<body>
<main class="spread">
  <section class="back-cover">
    <div class="synopsis">
      <p>The landscape of the publishing industry is changing. Gone are the days of coveted gatekeepers controlling content and dictating the messages being distributed. With the rise of technology, social media , self-publishing platforms, and independent bookstores, there are increased opportunities for people to share their ideas, messages, and stories with the world through books. The types of books that we’re publishing are also evolving — mini-books, audio books, journals, multi-author books, cook books, children’s books, comic books, coloring books, interactive books, tarot and oracle card decks are all expanding the podium for people to express ideas and influence the culture. More and more entrepreneurs are posturing themselves as thought leaders by leveraging this growing platform.</p>
      <p>But that doesn't mean it’s easy.</p>
      <p>Even with the expanding platforms and opportunities, only a fraction of people with publishing ambitions are able to achieve this coveted dream held by so many. It can be a daunting process for budding authors trying to maneuver through the writing, packaging, marketing, and publishing processes alone.</p>
      <p class="gap">In this book you'll find passionate, purpose-driven, and well-versed experts working in the various areas of publishing, eager to help open your eyes to the promise of publishing and effortlessly guide you through the process.</p>
    </div>
    <p class="publisher">Bright Lantern Publishing</p>
  </section>

  <section class="spine">
    <p class="spine-title">Write Onward! Veteran Editors Reveal Their Methods</p>
  </section>

  <section class="front-cover">
    <h1 class="front-title">
      <span class="lead">Write Onward!</span>
      <span class="line">Veteran</span>
      <span class="line">Editors</span>
      <span class="line">Reveal</span>
      <span class="line">Their</span>
      <span class="line">Methods</span>
    </h1>
    <div class="book-art" role="img" aria-label="Illustration of an open book with fanning pages, one side glowing white and one side dark navy">
      <div class="page-light"></div>
      <div class="page-dark"></div>
    </div>
    <ul class="authors">
      <li>Dana R. Holloway</li>
      <li>Dana R. Holloway</li>
      <li>Dana R. Holloway</li>
      <li>Dana R. Holloway</li>
    </ul>
  </section>
</main>
</body>
</html>
```